Maple Crest Holdings Inc.
Professional
Simon Oduya
Director
Lot 24 Hibiscus Lane Tremont,
Georgetown, Guyana
simon_d_oduya@mailnest-example.com
www.mchi-example.com
Logo and website

```html
<!DOCTYPE html>
<html lang="en">
<head>
<meta charset="utf-8">
<title>Maple Crest Holdings Inc. — Stationery</title>
<link rel="stylesheet" href="https://fonts.googleapis.com/css2?family=Arimo:wght@400;700&display=swap">
<style>
  :root {
    --navy: #1c2a5e;
    --blue: #1f4ea3;
    --blue-light: #e8eef8;
    --red: #c8102e;
    --red-dark: #7d0a16;
    --paper: #ffffff;
    --ink: #333a47;
    --rule: #9aa0aa;
    --backdrop: #e6e7ea;
  }
  * { box-sizing: border-box; margin: 0; padding: 0; }
  html, body { width: 1200px; height: 935px; overflow: hidden; }
  body { background: var(--backdrop); font-family: "Arimo", Arial, sans-serif; color: var(--ink); position: relative; }

  .sheet { position: absolute; background: var(--paper); box-shadow: 0 2px 8px rgba(0,0,0,.18); overflow: hidden; }

  /* header bars */
  .header-bars { position: absolute; top: 0; left: 0; display: flex; height: 12px; }
  .header-bars .bar-red { width: 22px; background: var(--red); }
  .header-bars .bar-blue { width: 150px; background: linear-gradient(90deg, var(--blue), rgba(31,78,163,0)); }

  /* brand */
  .brand { position: absolute; display: flex; align-items: center; gap: 6px; }
  .brand-dot { width: 18px; height: 18px; border-radius: 50%; background: var(--red); flex: none; }
  .brand-name { font-weight: 700; font-size: 13px; color: var(--navy); white-space: nowrap; }

  .footer-address { position: absolute; font-size: 7.5px; line-height: 1.5; color: var(--ink); }
  .footer-address .web { color: var(--red); font-weight: 700; }

  /* fax */
  .fax { left: 40px; top: 60px; width: 340px; height: 440px; }
  .fax-title { position: absolute; left: 26px; top: 110px; font-size: 26px; color: var(--ink); }
  .fax-fields { position: absolute; left: 26px; top: 160px; width: 250px; list-style: none; }
  .fax-fields li { display: flex; font-size: 10px; height: 24px; align-items: flex-end; }
  .fax-fields li span { flex: 1; border-bottom: 1px solid var(--rule); margin-left: 6px; height: 1px; margin-bottom: 3px; }
  .fax-checks { position: absolute; left: 26px; top: 275px; display: flex; gap: 26px; font-size: 10px; }
  .fax-checks label { display: flex; align-items: center; gap: 5px; }
  .fax-checks i { width: 9px; height: 9px; border: 1px solid var(--rule); background: #f2f2f2; }

  /* letterhead */
  .letterhead { left: 410px; top: 60px; width: 340px; height: 440px; }

  /* envelope */
  .envelope { left: 40px; top: 540px; width: 710px; height: 340px; }
  .envelope-flap { position: absolute; left: 0; top: 0; width: 100%; height: 110px; }
  .envelope .header-bars { top: 110px; height: 10px; }
  .envelope .header-bars .bar-blue { width: 230px; }

  /* cards */
  .card { position: absolute; left: 790px; width: 370px; height: 211px; box-shadow: 0 2px 8px rgba(0,0,0,.2); overflow: hidden; }
  .card-front { top: 60px; background: var(--paper); }
  .card-name-band { position: absolute; left: 190px; top: 56px; width: 180px; height: 22px; background: var(--navy); color: #fff; font-size: 10px; display: flex; align-items: center; padding-left: 12px; gap: 6px; }
  .card-name-band .role { font-size: 8px; opacity: .8; }
  .card-details { position: absolute; right: 14px; bottom: 20px; text-align: right; font-size: 7.5px; line-height: 1.6; }
  .card-details .web { color: var(--red); font-weight: 700; }

  .card-back { display: flex; flex-direction: column; justify-content: center; }
  .card-back-navy { top: 300px; background: var(--navy); }
  .card-back-red { top: 540px; background: linear-gradient(90deg, var(--red-dark), var(--red) 55%, var(--red-dark)); }
  .card-back-panel { position: relative; margin-left: 40px; height: 60px; background: linear-gradient(90deg, #fff 55%, rgba(255,255,255,.15)); }
  .card-back-panel .brand { left: 14px; top: 20px; }
  .card-tagline { margin: 16px 0 0 56px; color: #fff; font-size: 14px; letter-spacing: .5px; font-style: italic; }
  .card-tagline b { font-weight: 400; margin-right: 10px; }
  .card-web { margin: 12px 0 0 56px; color: #fff; font-size: 8px; }
</style>
</head>
<body>

<section class="sheet fax" aria-label="Fax cover sheet">
  <div class="header-bars"><div class="bar-red"></div><div class="bar-blue"></div></div>
  <div class="brand" style="left:26px;top:36px"><span class="brand-dot"></span><span class="brand-name">Maple Crest Holdings Inc.</span></div>
  <h1 class="fax-title">FAX</h1>
  <ul class="fax-fields">
    <li>To:<span></span></li>
    <li>Fax:<span></span></li>
    <li>Phone:<span></span></li>
    <li>Re:<span></span></li>
  </ul>
  <div class="fax-checks">
    <label><i></i>Urgent</label>
    <label><i></i>For Review</label>
  </div>
  <address class="footer-address" style="left:26px;bottom:20px;font-style:normal">
    Lot 24 Hibiscus Lane Tremont, Georgetown, Guyana<br>
    P. (555) 014-2207 &nbsp;C. (555) 018-3391 &nbsp;E. simon_d_oduya@mailnest-example.com<br>
    <span class="web">www.mchi-example.com</span>
  </address>
</section>

<section class="sheet letterhead" aria-label="Letterhead">
  <div class="header-bars"><div class="bar-red"></div><div class="bar-blue"></div></div>
  <div class="brand" style="left:26px;top:36px"><span class="brand-dot"></span><span class="brand-name">Maple Crest Holdings Inc.</span></div>
  <address class="footer-address" style="left:26px;bottom:20px;font-style:normal">
    Lot 24 Hibiscus Lane Tremont, Georgetown, Guyana<br>
    P. (555) 014-2207 &nbsp;C. (555) 018-3391 &nbsp;E. simon_d_oduya@mailnest-example.com<br>
    <span class="web">www.mchi-example.com</span>
  </address>
</section>

<section class="sheet envelope" aria-label="Envelope">
  <svg class="envelope-flap" viewBox="0 0 710 110" preserveAspectRatio="none" aria-hidden="true">
    <defs>
      <linearGradient id="flap" x1="0" x2="1" y1="0" y2="0">
        <stop offset="0" stop-color="#7d0a16"/>
        <stop offset=".5" stop-color="#c8102e"/>
        <stop offset="1" stop-color="#7d0a16"/>
      </linearGradient>
    </defs>
    <path d="M0 0 H710 V110 H0 Z" fill="url(#flap)"/>
    <path d="M0 0 L355 40 L710 0" fill="none" stroke="rgba(255,255,255,.18)" stroke-width="2"/>
  </svg>
  <div class="header-bars"><div class="bar-red"></div><div class="bar-blue"></div></div>
  <div class="brand" style="left:40px;top:140px"><span class="brand-dot"></span><span class="brand-name" style="font-size:16px">Maple Crest Holdings Inc.</span></div>
  <address class="footer-address" style="left:70px;bottom:28px;font-style:normal;font-size:8.5px">
    Lot 24 Hibiscus Lane Tremont, Georgetown, Guyana<br>
    <span class="web">www.mchi-example.com</span>
  </address>
</section>

<section class="card card-front" aria-label="Business card front">
  <div class="header-bars"><div class="bar-red"></div><div class="bar-blue"></div></div>
  <div class="brand" style="left:22px;top:30px"><span class="brand-dot"></span><span class="brand-name">Maple Crest Holdings Inc.</span></div>
  <div class="card-name-band"><strong>Simon Oduya</strong><span class="role">Director</span></div>
  <address class="card-details" style="font-style:normal">
    Lot 24 Hibiscus Lane Tremont, Georgetown, Guyana<br>
    P. (555) 014-2207 &nbsp;C. (555) 018-3391<br>
    simon_d_oduya@mailnest-example.com<br>
    <span class="web">www.mchi-example.com</span>
  </address>
</section>

<section class="card card-back card-back-navy" aria-label="Business card back, navy">
  <div class="card-back-panel"><div class="brand"><span class="brand-dot"></span><span class="brand-name" style="font-size:15px">Maple Crest Holdings Inc.</span></div></div>
  <p class="card-tagline"><b>Fast</b><b>Reliable</b><b>Efficient</b></p>
  <p class="card-web">www.mchi-example.com</p>
</section>

<section class="card card-back card-back-red" aria-label="Business card back, red">
  <div class="card-back-panel"><div class="brand"><span class="brand-dot"></span><span class="brand-name" style="font-size:15px">Maple Crest Holdings Inc.</span></div></div>
  <p class="card-tagline"><b>Fast</b><b>Reliable</b><b>Efficient</b></p>
  <p class="card-web">www.mchi-example.com</p>
</section>

</body>
</html>
```